Letterhead design of KESTREL POWER THRIFT INC.

we are a energy saving company doing the solar screen, radian barrier, attic insulation, double panel windows. Basically i need the design of the letterhead including my company name, business address, phone numbers, fax number and email address. Main thing i need it look like a huge company and look like very high class. thanks !!

Reason: Please send me more new design about my company! Thanks so much!!

Industry/Entity Type

Business

```html
<!DOCTYPE html>
<html lang="en">
<head>
<meta charset="utf-8">
<title>Kestrel Power Thrift Inc. — Letterhead</title>
<link rel="stylesheet" href="https://fonts.googleapis.com/css2?family=Tinos&display=swap">
<style>
  :root {
    --band-grey: #d1d1d3;
    --name-grey: #7d7d80;
    --footer-text: #a2a2a4;
    --paper: #ffffff;
    --bulb-light: #eef4f8;
    --bulb-mid: #d9e8f1;
    --bulb-edge: #e4e4e6;
    --accent-blue: #a9d3ec;
  }
  html, body {
    margin: 0;
    padding: 0;
    width: 848px;
    height: 1200px;
    overflow: hidden;
    background: var(--paper);
  }
  .letterhead {
    position: relative;
    width: 848px;
    height: 1200px;
    overflow: hidden;
    background: var(--paper);
    font-family: "Tinos", "Times New Roman", serif;
  }
  .header-wave {
    position: absolute;
    inset: 0 0 auto 0;
    width: 848px;
    height: 200px;
  }
  .company-name {
    font-family: "Tinos", "Times New Roman", serif;
    font-size: 31px;
    fill: var(--name-grey);
  }
  .header-bulbs {
    position: absolute;
    left: 650px;
    top: 12px;
    width: 160px;
    height: 138px;
    border-radius: 50%;
    background: radial-gradient(circle at 45% 40%, #e8f4fb 0%, var(--accent-blue) 70%, #8cc3e4 100%);
    opacity: 0.85;
  }
  .watermark-bulb {
    position: absolute;
    left: 0;
    top: 264px;
    width: 292px;
    height: 734px;
    border-radius: 0 150px 90px 0 / 0 320px 120px 0;
    background: linear-gradient(180deg, var(--bulb-light) 0%, var(--bulb-mid) 55%, var(--bulb-edge) 100%);
  }
  .footer-band {
    position: absolute;
    left: 0;
    bottom: 0;
    width: 848px;
    height: 100px;
    background: var(--band-grey);
    color: var(--footer-text);
    text-align: center;
    font-size: 18.5px;
    line-height: 32px;
    padding-top: 6px;
    box-sizing: border-box;
  }
  .footer-band p { margin: 0; }
</style>
</head>
<body>
<div class="letterhead">
  <svg class="header-wave" viewBox="0 0 848 200" aria-hidden="false">
    <path d="M0,0 H848 V192 C684,150 428,71 214,107 C114,125 43,150 0,168 Z" fill="var(--band-grey)"/>
    <defs>
      <path id="name-curve" d="M82,100 C240,66 440,88 650,172"/>
    </defs>
    <text class="company-name">
      <textPath href="#name-curve" textLength="575" lengthAdjust="spacing">KESTREL POWER THRIFT INC.</textPath>
    </text>
  </svg>

  <div class="header-bulbs" role="img" aria-label="Illustration of two light bulbs joined at their bases"></div>

  <div class="watermark-bulb" role="img" aria-label="Large faint illustration of a light bulb along the left edge"></div>

  <footer class="footer-band">
    <p>Address: 2280 Marlow Ave Suite #300 Houston, TEXAS 77099</p>
    <p>Phone: # 832 555 0148;&nbsp; Fax: # 281 555 0193</p>
    <p>Email: kestrelpowerthrift@example.com</p>
  </footer>
</div>
</body>
</html>
```